Label for LiPo Battery Product for RC Hobby Industry

We need your creativity for a new lithium battery label design. We aim to make our product visually appealing and distinct from competitors. Your design skills are crucial for this task, and we're excited to work with you.
Our main label feature is the colour tag profile, designed to easily identify battery category and power level with a 2-way colour band. Inspired by a tool company that uses a consistent colour profile to identify Phillips head sizing across their range.
The design should be modern, clear, convey speed and suitable for both professional and consumer markets.
Target Market(s)
RC, Drone, Camera community. 20-30 year old.
Industry/Entity Type
Battery, Drone Industry, RC Car
Requirements
Must have
- 2-Way colour tag identity profiling, clear text at 100% scale
Nice to have
- Text and graphic alignment. Comfortable padding and formatting. Colour tag profile, clear text."
Should not have
- Basic, stock looking image.

```html
<!DOCTYPE html>
<html lang="en">
<head>
<meta charset="utf-8">
<title>RX240 LiPo Battery Label</title>
<link rel="stylesheet" href="https://fonts.googleapis.com/css2?family=Orbitron:wght@700;900&family=Russo+One&display=swap">
<style>
  :root {
    --stage-top: #5e5e5e;
    --stage-bottom: #8a8a8a;
    --label-dark: #111317;
    --label-dark-2: #23262c;
    --band-blue-deep: #1d2a8a;
    --band-blue: #3a4fd0;
    --band-cyan: #38d8f0;
    --band-red: #ff2a4a;
    --band-red-deep: #b0102a;
    --ink-white: #ffffff;
    --ink-dark: #1c1c1c;
    --silver-1: #9a9a9a;
    --silver-2: #f2f2f2;
    --silver-3: #bdbdbd;
    --shade: rgba(0,0,0,0.45);
  }
  * { box-sizing: border-box; margin: 0; padding: 0; }
  html, body {
    width: 1200px; height: 960px; overflow: hidden;
    background: linear-gradient(180deg, var(--stage-top), var(--stage-bottom));
  }
  .label {
    position: absolute; left: 60px; top: 190px;
    width: 1080px; height: 580px;
    border-radius: 14px; overflow: hidden;
    background: linear-gradient(180deg, var(--label-dark-2), var(--label-dark) 60%, var(--label-dark-2));
    box-shadow: 6px 8px 14px var(--shade);
    font-family: "Russo One", sans-serif;
    color: var(--ink-white);
  }
  .label__header {
    position: absolute; left: 0; top: 0; width: 100%; height: 150px;
  }
  .product-name {
    position: absolute; left: 70px; top: 38px;
    font-size: 104px; line-height: 1; letter-spacing: -2px;
    color: var(--ink-white);
  }
  .brand-name {
    position: absolute; right: 66px; top: 66px;
    font-family: "Orbitron", sans-serif; font-weight: 900;
    font-size: 56px; letter-spacing: 4px; line-height: 1;
    color: var(--ink-white);
  }
  .power-band {
    position: absolute; left: 0; top: 150px; width: 100%; height: 230px;
    background:
      linear-gradient(90deg, rgba(56,216,240,0.35), transparent 25%, transparent 75%, rgba(56,216,240,0.45)),
      linear-gradient(180deg, var(--label-dark) 0%, var(--band-blue-deep) 30%, var(--band-blue) 55%, var(--band-blue-deep) 100%);
  }
  .capacity {
    position: absolute; left: 92px; top: 222px;
    font-size: 168px; line-height: 1; letter-spacing: -6px;
    text-shadow: 3px 5px 0 #9aa0aa, 6px 9px 10px var(--shade);
  }
  .capacity-meta {
    position: absolute; left: 700px; top: 220px;
    line-height: 0.9; text-align: center;
  }
  .capacity-meta__rate, .capacity-meta__unit {
    display: block; font-size: 84px; letter-spacing: -2px;
    text-shadow: 2px 4px 0 #9aa0aa, 4px 6px 8px var(--shade);
  }
  .spec-band {
    position: absolute; left: 0; top: 382px; width: 100%; height: 70px;
    background: linear-gradient(180deg, var(--band-red-deep), var(--band-red) 45%, #ff6a80 55%, var(--band-red-deep));
    display: flex; align-items: center; justify-content: center; gap: 22px;
    font-size: 46px; letter-spacing: 1px;
    text-shadow: 2px 3px 4px var(--shade);
  }
  .spec-band__divider {
    width: 4px; height: 52px; background: var(--ink-white); transform: skewX(-12deg);
  }
  .feature-strip {
    position: absolute; left: 0; bottom: 0; width: 100%; height: 72px;
    background: linear-gradient(90deg, var(--silver-1), var(--silver-2) 25%, var(--silver-3) 50%, var(--silver-2) 75%, var(--silver-1));
    border-top: 3px solid #d46a7a;
    display: flex; align-items: center; justify-content: center; gap: 16px;
    color: var(--ink-dark); font-size: 23px; letter-spacing: 0.5px;
  }
  .feature-strip__divider { width: 3px; height: 32px; background: var(--ink-dark); transform: skewX(-12deg); }
</style>
</head>
<body>
  <main class="label">
    <header class="label__header">
      <div class="product-name">RX240</div>
      <div class="brand-name">NORVAK</div>
    </header>

    <div class="power-band" role="img" aria-label="Blue band with cyan electric lightning streaks conveying power"></div>

    <div class="capacity">1300</div>
    <div class="capacity-meta">
      <span class="capacity-meta__rate">120C</span>
      <span class="capacity-meta__unit">mAh</span>
    </div>

    <div class="spec-band">
      <span>6 CELLS</span>
      <span class="spec-band__divider"></span>
      <span>22.2V</span>
      <span class="spec-band__divider"></span>
      <span>1300WH</span>
    </div>

    <footer class="feature-strip">
      <span>PERFORMANCE</span>
      <span class="feature-strip__divider"></span>
      <span>ARMOUR PROTECTION</span>
      <span class="feature-strip__divider"></span>
      <span>ADVANCED INSULATION</span>
    </footer>
  </main>
</body>
</html>
```